Information poster for parquet showroom

We are a parquet shop from germany and need some information poster for our showroom, to show our costumers some important information about parqut directly. The three posters are about reasons for parquet, and there are two types of paper on the subject. We would like to place the posters in a wooden frame. The design should be modern but simple. Enclosed I send you some of my ideas but it does not have to be like this. Can be completely different. I also send you some pictures of our showroom. 1st poster: Why parquet (dimension: 90x130 cm) Why parquet? - brings nature into your home - ecologically sustainable raw material - pleasantly warm - timeless% 26amp; high quality optics - durable% 26amp; reparable flooring - improved indoor climate - unique ride 2. Advantages oiled - tangible wood structure - natural appearance - scratches less present - partial repair possible advantage varnished - very easy-care - classic% 26amp; elegant appearance - protection against dirt and moisture - variable gloss level 3. Poster: overview of the hardness of different kinds of wood (dimension: 67x130 cm) wood hardness according to Brinell in N / mm² maple europ. 28 maple canadian. 35 birch 27 beech 33 oak 34 alder 17 ash 37 doussie 42 spruce 12 kambala 30 chestnut 18 pine 20 cherry european. 31 Larch 19 Merbau 44 Robinia 48 Sucupira 57 Elm 30 Wenge 45

```html
<!DOCTYPE html>
<html lang="de">
<head>
<meta charset="utf-8">
<title>Holzhärte nach Brinell</title>
<link rel="stylesheet" href="https://fonts.googleapis.com/css2?family=Oswald:wght@400;500;700&family=Open+Sans:wght@500&display=swap">
<style>
  :root {
    --orange: #e8951a;
    --ink: #111111;
    --white: #ffffff;
    --row-dark: #dddddd;
    --row-light: #f3f3f3;
    --backdrop: #d6d6d8;
  }
  * { box-sizing: border-box; margin: 0; padding: 0; }
  html, body {
    width: 1121px; height: 1200px; overflow: hidden;
    background: var(--backdrop);
  }
  .poster {
    position: absolute; left: 265px; top: 20px;
    width: 590px; height: 1160px;
    background: var(--white);
  }
  .poster-header {
    position: absolute; left: 0; top: 0; width: 100%; height: 198px;
    background: var(--orange);
  }
  .poster-title {
    position: absolute; left: 0; top: 24px; width: 100%;
    text-align: center;
    font-family: "Oswald", sans-serif; font-weight: 700;
    font-size: 92px; line-height: 1.2; letter-spacing: 4px;
    color: var(--white);
    text-shadow: 2px 3px 0 rgba(0,0,0,0.35);
  }
  .poster-subtitle {
    position: absolute; left: 66px; top: 127px; width: 460px; height: 36px;
    border-radius: 18px; background: var(--ink);
    text-align: center;
    font-family: "Open Sans", sans-serif; font-weight: 500;
    font-size: 27px; line-height: 36px; color: var(--white);
  }
  .hardness-list {
    position: absolute; left: 0; top: 213px; width: 100%;
    list-style: none;
  }
  .hardness-row {
    position: relative; height: 48.1px;
    background: var(--row-dark);
  }
  .hardness-row:nth-child(even) { background: var(--row-light); }
  .wood-name {
    position: absolute; right: calc(100% - 149px); top: 0;
    font-family: "Oswald", sans-serif; font-weight: 400;
    font-size: 26px; line-height: 48px; letter-spacing: -0.5px;
    color: var(--ink); white-space: nowrap;
  }
  .hardness-bar {
    position: absolute; left: 167px; top: 17px; height: 14px;
    width: calc(var(--v) * 6.6px);
    background: var(--ink);
  }
  .hardness-value {
    position: absolute; right: -17px; top: -10px;
    width: 34px; height: 34px; border-radius: 50%;
    background: var(--ink); border: 3px solid var(--orange);
    font-family: "Oswald", sans-serif; font-weight: 400;
    font-size: 19px; line-height: 28px; text-align: center;
    color: var(--white);
  }
  .hardness-row:nth-child(even) .wood-name { color: var(--orange); font-weight: 500; }
  .hardness-row:nth-child(even) .hardness-bar { background: var(--orange); }
  .hardness-row:nth-child(even) .hardness-value {
    background: var(--orange); border-color: var(--ink); color: var(--ink);
  }
  .poster-footer {
    position: absolute; left: 0; bottom: 0; width: 100%; height: 18px;
    background: var(--orange);
  }
</style>
</head>
<body>
  <main class="poster">
    <header class="poster-header">
      <h1 class="poster-title">HOLZHÄRTE</h1>
      <p class="poster-subtitle">nach Brinell in N/mm²</p>
    </header>
    <ol class="hardness-list">
      <li class="hardness-row" style="--v:57"><span class="wood-name">SUCUPIRA</span><span class="hardness-bar"><span class="hardness-value">57</span></span></li>
      <li class="hardness-row" style="--v:48"><span class="wood-name">ROBINIE</span><span class="hardness-bar"><span class="hardness-value">48</span></span></li>
      <li class="hardness-row" style="--v:45"><span class="wood-name">WENGE</span><span class="hardness-bar"><span class="hardness-value">45</span></span></li>
      <li class="hardness-row" style="--v:44"><span class="wood-name">MERBAU</span><span class="hardness-bar"><span class="hardness-value">44</span></span></li>
      <li class="hardness-row" style="--v:42"><span class="wood-name">DOUSSIE</span><span class="hardness-bar"><span class="hardness-value">42</span></span></li>
      <li class="hardness-row" style="--v:37"><span class="wood-name">ESCHE</span><span class="hardness-bar"><span class="hardness-value">37</span></span></li>
      <li class="hardness-row" style="--v:35"><span class="wood-name">AHORN KAN.</span><span class="hardness-bar"><span class="hardness-value">35</span></span></li>
      <li class="hardness-row" style="--v:34"><span class="wood-name">EICHE</span><span class="hardness-bar"><span class="hardness-value">34</span></span></li>
      <li class="hardness-row" style="--v:33"><span class="wood-name">BUCHE</span><span class="hardness-bar"><span class="hardness-value">33</span></span></li>
      <li class="hardness-row" style="--v:31"><span class="wood-name">KIRSCHE EU.</span><span class="hardness-bar"><span class="hardness-value">31</span></span></li>
      <li class="hardness-row" style="--v:30"><span class="wood-name">KAMBALA</span><span class="hardness-bar"><span class="hardness-value">30</span></span></li>
      <li class="hardness-row" style="--v:30"><span class="wood-name">ULME</span><span class="hardness-bar"><span class="hardness-value">30</span></span></li>
      <li class="hardness-row" style="--v:28"><span class="wood-name">AHORN EU.</span><span class="hardness-bar"><span class="hardness-value">28</span></span></li>
      <li class="hardness-row" style="--v:27"><span class="wood-name">BIRKE</span><span class="hardness-bar"><span class="hardness-value">27</span></span></li>
      <li class="hardness-row" style="--v:20"><span class="wood-name">KIEFER</span><span class="hardness-bar"><span class="hardness-value">20</span></span></li>
      <li class="hardness-row" style="--v:19"><span class="wood-name">LÄRCHE</span><span class="hardness-bar"><span class="hardness-value">19</span></span></li>
      <li class="hardness-row" style="--v:18"><span class="wood-name">KASTANIE</span><span class="hardness-bar"><span class="hardness-value">18</span></span></li>
      <li class="hardness-row" style="--v:17"><span class="wood-name">ERLE</span><span class="hardness-bar"><span class="hardness-value">17</span></span></li>
      <li class="hardness-row" style="--v:12"><span class="wood-name">FICHTE</span><span class="hardness-bar"><span class="hardness-value">12</span></span></li>
    </ol>
    <footer class="poster-footer"></footer>
  </main>
</body>
</html>
```